Voltarey - Flyer design

Description -
Motorhome and Caravan EWOFs
Recreational Vehicles (such as caravans, motorhomes, RVs, Boats etc) and Relocatable buildings that can be connected to an electricity supply must be regularly checked for electrical safety. An EWOF needs to be issued every 4 years.
Pre-purchase house inspections
A pre-purchase electrical inspection prior to buying a home can be used to identify any dangerous and unsafe electrical parts of the installation that may be costly to repair once the property has been purchased. Giving you peace of mind when buying your new home.
High risk Electrical inspections
All Prescribed Electrical Work that falls under the High Risk category must be inspected by a Registered Electrical Inspector and have a Record of Inspection certificate issued.
Electric Vehicle Chargers
Any electrical vehicle charger that can be accessed by the public (ie in a non-domestic situation) must be periodically inspected and certified every 12 months.
General Electrical Services
Domestic and commercial - We do new builds, Renovations, Maintenance and more!
Dean Fowler - Electrician and Electrical Inspector
Ph - 0227839152
Dean@voltarey.co.nz
Auckland
------
I also want there to be a few symbols similar to the files I have attached.
The main areas that I am hoping to find work is with caravans/motohomes and EV car chargers so these symbols are quite important.
Thanks so much

```html
<!DOCTYPE html>
<html lang="en">
<head>
<meta charset="utf-8">
<title>Dean Fowler – Electrician &amp; Electrical Inspector</title>
<link rel="stylesheet" href="https://fonts.googleapis.com/css2?family=Anton&family=Oswald:wght@400&family=Poppins:ital,wght@0,400;0,600;0,700;0,800;1,800&display=swap">
<style>
  :root {
    --green: #8bc53f;
    --panel: #646464;
    --ink: #111111;
    --grey-text: #5e5e5e;
    --white: #ffffff;
    --art-soft: #e4efd6;
  }
  * { margin: 0; padding: 0; box-sizing: border-box; }
  html, body { width: 900px; height: 1200px; overflow: hidden; background: var(--white); }
  .flyer {
    position: relative; width: 900px; height: 1200px; overflow: hidden;
    background: var(--white); font-family: "Poppins", sans-serif; color: var(--ink);
  }
  .abs { position: absolute; }

  .name {
    left: 66px; top: 80px; font-family: "Anton", sans-serif; font-size: 96px;
    line-height: 1; color: var(--green); letter-spacing: -1px; white-space: nowrap;
  }
  .role {
    left: 80px; top: 198px; font-weight: 800; font-style: italic; font-size: 24px;
    letter-spacing: -0.3px; white-space: nowrap;
  }
  .brand { left: 604px; top: 84px; display: flex; align-items: center; gap: 12px; }
  .brand-square { width: 22px; height: 22px; background: var(--green); }
  .brand-name { font-weight: 600; font-size: 36px; color: #555555; line-height: 1; }

  .art {
    border-radius: 12px;
    background: radial-gradient(circle at 40% 55%, var(--art-soft), rgba(255,255,255,0) 70%);
  }
  .art-dark { background: radial-gradient(circle at 50% 50%, #7a7a7a, var(--panel) 75%); border-radius: 12px; }
  .art-plug-top { left: 707px; top: 156px; width: 193px; height: 186px; }
  .art-plug-bottom { left: 843px; top: 1116px; width: 44px; height: 84px; background: linear-gradient(#2a2a2a, #111); border-radius: 10px 10px 0 0; }

  .services-panel {
    left: 0; top: 303px; width: 394px; height: 846px; background: var(--panel);
    border-radius: 0 52px 52px 0;
  }
  .service-title {
    font-weight: 700; font-size: 22px; line-height: 35px; letter-spacing: 1.2px; color: var(--white);
  }
  .service-title.dark { color: var(--panel); font-size: 27px; line-height: 40.5px; }
  .copy { font-size: 15.4px; line-height: 21.5px; color: var(--white); }
  .copy.dark { color: var(--grey-text); }
  .copy ul { list-style: none; padding-left: 29px; }
  .copy li { position: relative; }
  .copy li::before { content: "•"; position: absolute; left: -14px; }

  .cta {
    left: 420px; top: 950px; width: 446px; text-align: center; font-weight: 800; font-style: italic;
    font-size: 25.5px; line-height: 29px; letter-spacing: -0.3px;
  }
  .contact-btn {
    left: 447px; top: 1049px; width: 110px; height: 30px; border-radius: 8px; background: var(--green);
    color: var(--white); font-size: 12.5px; display: flex; align-items: center; justify-content: center;
  }
  .phone { left: 447px; top: 1088px; width: 110px; text-align: center; font-family: "Oswald", sans-serif; font-size: 23px; }
  .icon-dot {
    width: 37px; height: 37px; border-radius: 50%; background: var(--green);
    display: flex; align-items: center; justify-content: center;
  }
  .info-label { font-size: 14.5px; line-height: 19px; letter-spacing: 0.5px; }
  .info-value { font-size: 14px; font-weight: 700; line-height: 19px; letter-spacing: 0.3px; }
</style>
</head>
<body>
<main class="flyer">
  <h1 class="abs name">DEAN FOWLER</h1>
  <p class="abs role">Electrician &amp; Electrical Inspector</p>

  <div class="abs brand">
    <span class="brand-square"></span>
    <span class="brand-name">Voltarey</span>
  </div>

  <div class="abs art art-plug-top" role="img" aria-label="Electric plug illustration with spark burst and green halftone dots"></div>

  <section class="abs services-panel" aria-label="Inspection services"></section>

  <div class="abs art-dark" style="left:25px;top:362px;width:142px;height:94px" role="img" aria-label="Caravan with power connection icon"></div>
  <h2 class="abs service-title" style="left:188px;top:364px">Motorhome<br>&amp; Caravan<br>EWOFs</h2>
  <div class="abs copy" style="left:25px;top:472px;width:360px">
    Ensure your motorhomes, caravans, RVs, boats, and relocatable buildings are electrically safe.
    <ul>
      <li>Compliance required every 4 years.</li>
      <li>Stay worry-free when connecting to power supplies.</li>
    </ul>
  </div>

  <div class="abs art-dark" style="left:33px;top:651px;width:134px;height:101px" role="img" aria-label="House with lightning bolt and plug icon"></div>
  <h2 class="abs service-title" style="left:181px;top:651px">Pre-Purchase<br>House<br>Inspections</h2>
  <p class="abs copy" style="left:25px;top:773px;width:340px">Buy with peace of mind. Identify dangerous or costly electrical issues before purchasing your new home.</p>

  <svg class="abs" style="left:25px;top:864px" width="127" height="115" viewBox="0 0 127 115" aria-hidden="true">
    <path d="M63.5 6 L121 105 H6 Z" fill="none" stroke="#fff" stroke-width="7" stroke-linejoin="round"/>
    <path d="M70 30 L52 68 H66 L58 96 L80 58 H66 Z" fill="#fff"/>
  </svg>
  <h2 class="abs service-title" style="left:188px;top:868px">High-Risk<br>Electrical<br>Inspections</h2>
  <p class="abs copy" style="left:25px;top:998px;width:345px">All Prescribed Electrical Work in the high-risk category must be inspected by a Registered Electrical Inspector with an official Record of Inspection (ROI).</p>

  <div class="abs art" style="left:460px;top:394px;width:177px;height:126px;background:linear-gradient(135deg,#ececec,#d6d6d6)" role="img" aria-label="Electric car plugged into a charging station icon"></div>
  <h2 class="abs service-title dark" style="left:694px;top:405px">Electric<br>Vehicle<br>Chargers</h2>
  <div class="abs copy dark" style="left:455px;top:537px;width:380px">
    Ensure safety and compliance for public-access EV chargers.
    <ul>
      <li>Required inspection every 12 months.</li>
      <li>Certification ensures reliable and safe charging.</li>
    </ul>
  </div>

  <div class="abs art" style="left:472px;top:688px;width:116px;height:121px;background:linear-gradient(135deg,#ececec,#d6d6d6)" role="img" aria-label="Electrician with test meter icon"></div>
  <h2 class="abs service-title dark" style="left:694px;top:700px">General<br>Electrical<br>Services</h2>
  <div class="abs copy dark" style="left:455px;top:832px;width:380px">
    Domestic and commercial services, including:
    <ul>
      <li>New Builds</li>
      <li>Renovations</li>
      <li>Maintenance and more!</li>
    </ul>
  </div>

  <p class="abs cta">Contact Dean Fowler Today for Professional Electrical Services!</p>

  <div class="abs contact-btn">CONTACT US</div>
  <p class="abs phone">022 783 9152</p>

  <div class="abs icon-dot" style="left:581px;top:1038px">
    <svg width="20" height="20" viewBox="0 0 20 20" aria-hidden="true">
      <path d="M2 10 L10 3 L18 10 M5 8 V17 H15 V8" fill="none" stroke="#fff" stroke-width="2" stroke-linejoin="round"/>
      <rect x="8.5" y="11.5" width="3" height="5.5" fill="#fff"/>
    </svg>
  </div>
  <p class="abs info-label" style="left:635px;top:1035px">Visit Our Location</p>
  <p class="abs info-value" style="left:635px;top:1054px">123 Anywhere St., Auckland</p>

  <div class="abs icon-dot" style="left:581px;top:1088px">
    <svg width="20" height="16" viewBox="0 0 20 16" aria-hidden="true">
      <rect x="1" y="2" width="18" height="12" fill="none" stroke="#fff" stroke-width="1.8"/>
      <path d="M1 2 L10 9 L19 2" fill="none" stroke="#fff" stroke-width="1.8"/>
    </svg>
  </div>
  <p class="abs info-label" style="left:635px;top:1087px">Mail Us</p>
  <p class="abs info-value" style="left:635px;top:1106px">Dean@voltarey.co.nz</p>

  <div class="abs art-plug-bottom" role="img" aria-label="Black electric plug on a cord"></div>
</main>
</body>
</html>
```